Trolvex.ai

Australian based application building technology company. website (trolvex.ai) servicing the retail and shopping industries, IoT
Similar services to https://quarnel.com/.
Logo attached

Target Market(s)

Technology Retail

Industry/Entity Type

It Company

Number of Pages Required

2 page

Font styles to use
Other font styles liked:
• We will supply

Colors
ec1f27

Requirements
Must have
• responsive, extra small, small, medium, large, wide
Nice to have
• Modern, sophisticated, current and ON trende
Should not have
• Over saturation, keep it simple, smart and easy navigation

```html
<!DOCTYPE html>
<html lang="en">
<head>
<meta charset="utf-8">
<title>Trolvex — Smart retail technology</title>
<link href="https://fonts.googleapis.com/css2?family=Open+Sans:wght@300;400;600;700&display=swap" rel="stylesheet">
<style>
:root{
  --red:#ec1f27;
  --red-deep:#a8060b;
  --red-hero:#c90f16;
  --band:#e9e7e3;
  --ink:#2b2b2b;
  --body:#6a6a6a;
  --white:#ffffff;
  --line:#dddddd;
  --media-light:#eeeeee;
  --media-mid:#dcdcdc;
}
*{box-sizing:border-box;margin:0;padding:0}
html,body{width:1200px;height:4100px;overflow:hidden}
body{position:relative;font-family:"Open Sans",Arial,sans-serif;color:var(--ink);background:var(--white)}
.abs{position:absolute}
p.copy{font-size:12px;line-height:33px;color:var(--body)}
.btn{position:absolute;display:flex;align-items:center;justify-content:center;gap:8px;border-radius:22px;background:var(--red);color:var(--white);font-size:11px;font-weight:700;letter-spacing:.5px;text-transform:uppercase;height:42px}

/* hero */
.hero{position:absolute;left:0;top:0;width:1200px;height:560px;background:radial-gradient(ellipse at 50% 45%,var(--red-hero) 0%,var(--red-deep) 80%)}
.brand{position:absolute;display:flex;align-items:center;gap:10px;font-weight:700;font-size:26px;letter-spacing:.5px}
.brand .dot{width:16px;height:16px;border-radius:50%}
.hero .brand{left:96px;top:48px;color:var(--white)}
.hero .brand .dot{background:var(--white)}
.nav{position:absolute;top:58px;left:424px}
.nav a{position:absolute;color:var(--white);font-size:13px;text-decoration:none;white-space:nowrap}
.nav a.active{border-bottom:2px solid var(--white);padding-bottom:6px}
.pill{position:absolute;top:46px;height:40px;border-radius:20px;font-size:11px;font-weight:700;display:flex;align-items:center;justify-content:center;text-transform:uppercase}
.pill.solid{left:896px;width:108px;background:var(--white);color:var(--red)}
.pill.ghost{left:1016px;width:86px;border:2px solid var(--white);color:var(--white)}
.hero-media{position:absolute;left:250px;top:135px;width:740px;height:290px;background:radial-gradient(ellipse at 50% 50%,rgba(60,80,150,.35) 0%,rgba(160,10,20,0) 75%)}
.hero-tag{position:absolute;top:448px;width:1200px;text-align:center;color:var(--white);font-weight:300;font-size:34px}

/* sections */
.band{position:absolute;left:0;width:1200px}
.band.grey{background:var(--band)}
.media{position:absolute;border-radius:4px}
.media.light{background:linear-gradient(135deg,var(--media-light),var(--media-mid))}
.media.red{background:linear-gradient(135deg,#d2171e,#a80d13)}
.h-title{position:absolute;font-weight:400;font-size:36px;line-height:44px;color:var(--ink)}
.h-bold{position:absolute;font-weight:700;font-size:18px;line-height:35px;color:var(--ink)}
.h-red{position:absolute;font-weight:400;font-size:17px;line-height:33px;color:var(--red)}
.cta{position:absolute;left:0;top:3403px;width:1200px;height:273px;background:var(--red);color:var(--white);text-align:center}

/* footer */
.footer{position:absolute;left:0;top:3676px;width:1200px;height:424px;background:var(--white)}
.footer .brand{left:96px;top:84px;color:var(--red)}
.footer .brand .dot{background:var(--red)}
.contact{position:absolute;left:96px;font-size:12px;color:var(--body);display:flex;gap:12px;align-items:flex-start;line-height:27px}
.contact svg{margin-top:6px}
.fcol{position:absolute;top:66px}
.fcol h4{font-size:13px;font-weight:700;letter-spacing:.5px;text-transform:uppercase;color:var(--ink);margin-bottom:18px}
.fcol li{list-style:none;font-size:12px;color:var(--body);height:34.5px;display:flex;align-items:center;gap:14px}
.fcol li::before{content:"";width:0;height:0;border-left:5px solid var(--ink);border-top:3.5px solid transparent;border-bottom:3.5px solid transparent}
.email-field{position:absolute;left:839px;top:109px;width:260px;height:39px;border:1px solid var(--line);font-size:11px;color:#999;padding-left:18px;display:flex;align-items:center}
.email-field svg{position:absolute;right:12px}
.subscribe{position:absolute;left:839px;top:161px;width:107px;height:36px;background:var(--red);color:var(--white);font-size:11px;font-weight:700;display:flex;align-items:center;justify-content:center}
.socials{position:absolute;left:839px;top:226px;display:flex;gap:6px}
.socials span{width:30px;height:30px;border-radius:50%}
.rule{position:absolute;left:96px;top:309px;width:1008px;height:1px;background:var(--line)}
.legal{position:absolute;top:350px;width:1200px;text-align:center;font-size:11px;color:var(--body)}
</style>
</head>
<body>

<header class="hero">
  <div class="brand"><span class="dot"></span>TROLVEX</div>
  <nav class="nav">
    <a class="active" style="left:0;top:0">Home</a>
    <a style="left:82px;top:0">About us</a>
    <a style="left:183px;top:0">Products</a>
    <a style="left:281px;top:0">Resources</a>
    <a style="left:388px;top:0">Support</a>
  </nav>
  <div class="pill solid">Get started</div>
  <div class="pill ghost">Sign in</div>
  <div class="hero-media" role="img" aria-label="Photo of two blue beacon devices either side of a smartphone playing a store map video"></div>
  <p class="hero-tag">This will make you Trolvex</p>
</header>

<section class="band" style="top:560px;height:560px">
  <div class="media light" role="img" aria-label="Photo of two smartphones showing a product offer and a store map" style="left:104px;top:80px;width:346px;height:410px"></div>
  <h2 class="h-title" style="left:490px;top:131px">Welcome to Trolvex</h2>
  <p class="h-red" style="left:490px;top:183px;font-size:15px">We service to the retail and shopping industries, IoT firms etc.</p>
  <p class="copy abs" style="left:490px;top:224px;width:660px">Sed ut perspiciatis unde omnis iste natus error sit voluptatem accusantium doloremque laudantium, totam rem aperiam, eaque ipsa quae ab illo inventore veritatis et quasi architecto beatae vitae dicta sunt explicabo. Nemo enim ipsam voluptatem quia voluptas sit aspernatur aut odit aut fugit, sed quia consequuntur magni dolores eos qui ratione voluptatem sequi nesciunt.</p>
  <div class="btn" style="left:490px;top:386px;width:170px">Upgrade your app</div>
</section>

<section class="band grey" style="top:1120px;height:460px">
  <div class="media light" role="img" aria-label="Photo of a hand holding a smartphone with an indoor navigation map" style="left:110px;top:40px;width:275px;height:420px"></div>
  <h2 class="h-bold" style="left:443px;top:83px;width:683px">Ut enim ad minima veniam, quis nostrum exercitationem ullam corporis suscipit laboriosam, nisi ut aliquid ex ea commodi consequatur</h2>
  <p class="copy abs" style="left:443px;top:160px;width:683px">But I must explain to you how all this mistaken idea of denouncing pleasure and praising pain was born and I will give you a complete account of the system, and expound the actual teachings of the great explorer of the truth, the master-builder of human happiness. No one rejects, dislikes, or avoids pleasure itself, because it is pleasure, but because those who do not know how to pursue pleasure that are extremely painful.</p>
  <div class="btn" style="left:443px;top:323px;width:170px">Read more info</div>
</section>

<section class="band" style="top:1580px;height:585px">
  <div class="media light" role="img" aria-label="Photo of two smartphones showing a mall map with a location pin" style="left:104px;top:87px;width:336px;height:410px"></div>
  <h2 class="h-red" style="left:490px;top:141px;width:660px">Ullam corporis suscipit laboriosam, nisi ut aliquid ex ea commodi consequatu Quis autem vel eum iure reprehenderit qui in ea voluptate</h2>
  <p class="copy abs" style="left:490px;top:216px;width:660px">Sed ut perspiciatis unde omnis iste natus error sit voluptatem accusantium doloremque laudantium, totam rem aperiam, eaque ipsa quae ab illo inventore veritatis et quasi architecto beatae vitae dicta sunt explicabo. Nemo enim ipsam voluptatem quia voluptas sit aspernatur aut odit aut fugit, sed quia consequuntur magni dolores eos qui ratione voluptatem sequi nesciunt.</p>
  <div class="btn" style="left:490px;top:375px;width:170px">Find the location</div>
</section>

<section class="band grey" style="top:2165px;height:781px">
  <div class="media red" role="img" aria-label="Photo of a laptop showing a promotion about car space navigation" style="left:350px;top:76px;width:503px;height:369px"></div>
  <h2 class="h-title" style="left:0;top:477px;width:1200px;text-align:center;font-size:34px">Manage everything with ease</h2>
  <p class="copy abs" style="left:232px;top:535px;width:737px;text-align:center">Nam libero tempore, cum soluta nobis est eligendi optio cumque nihil impedit quo minus id quod maxime placeat facere possimus, omnis voluptas assumenda est, omnis dolor repellendus. Temporibus autem quibusdam et aut officiis debitis aut rerum necessitatibus saepe eveniet ut et voluptates repudiandae sint et molestiae non recusandae. Itaque earum rerum hic tenetur.</p>
  <div class="btn" style="left:487px;top:650px;width:225px;height:48px">
    <svg width="12" height="12" viewBox="0 0 12 12" aria-hidden="true"><path d="M6 1 L11 10 H1 Z" fill="#fff"/></svg>
    Download all features
  </div>
</section>

<section class="band" style="top:2946px;height:457px">
  <div class="media red" role="img" aria-label="Photo of a tablet on a stand showing real-time shopping online experiences" style="left:109px;top:74px;width:377px;height:273px"></div>
  <h2 class="h-red" style="left:519px;top:125px;font-size:24px;font-weight:600;line-height:34px">ONLINE EXPERIENCES</h2>
  <p class="copy abs" style="left:519px;top:169px;width:600px">Sed ut perspiciatis unde omnis iste natus error sit voluptatem accusantium doloremque laudantium, totam rem aperiam, eaque ipsa quae ab illo inventore veritatis et quasi architecto beatae vitae dicta sunt explicabo. Nemo enim ipsam voluptatem quia voluptas sit aspernatur aut odit aut fugit, sed quia consequuntur magni dolores eos qui ratione voluptatem sequi nesciunt.</p>
  <div class="btn" style="left:519px;top:325px;width:140px">Learn more</div>
</section>

<section class="cta">
  <h2 class="abs" style="left:0;top:48px;width:1200px;font-size:24px;font-weight:600">Ready to get started?</h2>
  <p class="abs" style="left:280px;top:102px;width:640px;font-size:11.5px;line-height:22px">Sint et molestiae non recusandae. Itaque earum rerum hic tenetur a sapiente delectus, ut aut reiciendis voluptatibus maiores alias consequatur aut perferendis doloribus asperiores repellat</p>
  <div class="btn" style="left:516px;top:177px;width:168px;background:var(--white);color:var(--red)">Get started</div>
</section>

<footer class="footer">
  <div class="brand"><span class="dot"></span>TROLVEX</div>
  <div class="contact" style="top:150px">
    <svg width="14" height="16" viewBox="0 0 14 16" aria-hidden="true"><path d="M7 1a5 5 0 0 0-5 5c0 4 5 9 5 9s5-5 5-9a5 5 0 0 0-5-5z" fill="none" stroke="#555" stroke-width="1.4"/><circle cx="7" cy="6" r="1.8" fill="#555"/></svg>
    <span>12 Arcade Lane<br>Doloremque laudantium</span>
  </div>
  <div class="contact" style="top:204px">
    <svg width="14" height="14" viewBox="0 0 14 14" aria-hidden="true"><path d="M3 1l2.5 3-1.5 1.5c1 2 2.5 3.5 4.5 4.5L10 8.5l3 2.5-1.5 2C6 12.5 1.5 8 1 2.5z" fill="none" stroke="#555" stroke-width="1.3"/></svg>
    <span>Phone: (555) 013-7740</span>
  </div>
  <div class="contact" style="top:241px">
    <svg width="15" height="12" viewBox="0 0 15 12" aria-hidden="true"><rect x="1" y="1" width="13" height="10" fill="none" stroke="#555" stroke-width="1.3"/><path d="M1 1l6.5 5.5L14 1" fill="none" stroke="#555" stroke-width="1.3"/></svg>
    <span>hello@trolvex.ai</span>
  </div>

  <div class="fcol" style="left:424px">
    <h4>Quick links</h4>
    <ul><li>Home</li><li>About Us</li><li>Products</li><li>Blog</li><li>Contact Us</li></ul>
  </div>
  <div class="fcol" style="left:618px">
    <h4>Other links</h4>
    <ul><li>Information</li><li>Privacy policy</li><li>Sitemap</li><li>My Account</li><li>Terms and Conditions</li></ul>
  </div>
  <div class="fcol" style="left:839px">
    <h4>Our newsletter</h4>
  </div>
  <div class="email-field">Your email
    <svg width="13" height="10" viewBox="0 0 13 10" aria-hidden="true"><rect width="13" height="10" fill="#333"/><path d="M0 0l6.5 5L13 0" fill="none" stroke="#fff" stroke-width="1"/></svg>
  </div>
  <div class="subscribe">SUBSCRIBE</div>
  <div class="socials" aria-label="Social links">
    <span style="background:#3b5a9a"></span>
    <span style="background:#29a9e1"></span>
    <span style="background:#d34836"></span>
    <span style="background:#e02a20"></span>
    <span style="background:#0077b5"></span>
    <span style="background:#1ab7ea"></span>
  </div>
  <div class="rule"></div>
  <p class="legal">© copyright 2017 Trolvex . All Rights Reserved</p>
</footer>

</body>
</html>
```